KV MERCANTILE HOLDINGS LETTERHEAD

I need letterhead for "KV Mercantile holdings LLC" ...

logo attached to project...

Company Info:
418 North Larkmoor Avenue, Suite 7B
Chicago, Illinois 60417
ofc 312-555-0148
facsimile 312-555-0193
www.kvmercantileholdings.example
info@kvmercantileholdings.example

I have multiple projects listed.. see below:

Business cards for amber ledge partners llc
letterhead
envelopes

Business cards for KV Mercantile LLC
letterhead
envelopes

```html
<!DOCTYPE html>
<html lang="en">
<head>
<meta charset="utf-8">
<title>KV Mercantile Holdings LLC – Letterhead</title>
<link rel="stylesheet" href="https://fonts.googleapis.com/css2?family=Crimson+Text:wght@400;600&display=swap">
<style>
  :root {
    --backdrop: #d9d9d9;
    --paper: #ffffff;
    --brand-navy: #03437a;
    --brand-ink: #1f4c82;
    --footer-text: #ffffff;
    --footer-label: #a9bfd8;
  }
  * { margin: 0; padding: 0; box-sizing: border-box; }
  html, body {
    width: 1200px;
    height: 1000px;
    overflow: hidden;
    background: var(--backdrop);
    font-family: "Crimson Text", Georgia, serif;
  }
  .letterhead {
    position: absolute;
    left: 235px;
    top: 26px;
    width: 728px;
    height: 943px;
    background: var(--paper);
  }
  .brand {
    position: absolute;
    top: 100px;
    left: 0;
    right: 0;
    display: flex;
    justify-content: center;
    align-items: center;
    gap: 10px;
    color: var(--brand-ink);
  }
  .brand-mark {
    width: 12px;
    height: 12px;
    border-radius: 50%;
    background: var(--brand-ink);
  }
  .brand-name {
    font-size: 21px;
    font-weight: 400;
    letter-spacing: 0.06em;
    text-transform: uppercase;
  }
  .footer-band {
    position: absolute;
    left: 0;
    right: 0;
    bottom: 0;
    height: 119px;
    background: var(--brand-navy);
    color: var(--footer-text);
    text-align: center;
    padding-top: 30px;
  }
  .footer-address {
    font-size: 13.5px;
    line-height: 20px;
  }
  .footer-phones {
    font-size: 13.5px;
    line-height: 20px;
  }
  .footer-phones .label {
    color: var(--footer-label);
    font-weight: 600;
  }
  .footer-phones .divider {
    margin: 0 6px;
  }
  .footer-web {
    font-size: 16px;
    line-height: 26px;
    letter-spacing: 0.02em;
  }
</style>
</head>
<body>
  <main class="letterhead">
    <header class="brand">
      <span class="brand-mark" aria-hidden="true"></span>
      <span class="brand-name">KV Mercantile Holdings LLC</span>
    </header>

    <footer class="footer-band">
      <p class="footer-address">418 North Larkmoor Avenue, Suite 7B, Chicago, Illinois 60417</p>
      <p class="footer-phones">
        <span class="label">Office:</span> 312-555-0148
        <span class="divider">|</span>
        <span class="label">Facsimile:</span> 312-555-0193
      </p>
      <p class="footer-web">www.kvmercantileholdings.example</p>
    </footer>
  </main>
</body>
</html>
```